I need a Label design for my copper 71 kombucha brand that is launching soon

I want a label to go on my copper 71 kombucha bottle.
I have a logo image uploaded in the files but I am open to changes to this logo or even a completely New one if you think you can do better. This logo is based on the idea of an s-shaped naga. I particularly like the nagas from temples in luang prabang.
I also want to include the slogan - dare to be delicious.
The label should be some kind of oval at 80mm high by 70mm wide.
The label will go on a clear glass bottle. The kombucha will be visible and comes in different shades of red,yellow and purple.
The word kombucha should be clearly visible.
i want a very colorful, playful label. I'm very keen to see your ideas and I want something original.
Fermented foods and beverages

```html
<!DOCTYPE html>
<html lang="en">
<head>
<meta charset="utf-8">
<title>copper 71 Kombucha – Label Range</title>
<link rel="stylesheet" href="https://fonts.googleapis.com/css2?family=Kalam:wght@700&family=Barlow+Condensed:wght@500;700&display=swap">
<style>
  :root {
    --paper: #ffffff;
    --label-base: #fbdcc2;
    --label-edge: #fde8d7;
    --plum: #8a4a9c;
    --berry: #e0303f;
    --tangerine: #f07b1a;
  }
  html, body {
    margin: 0;
    width: 946px;
    height: 1200px;
    overflow: hidden;
    background: var(--paper);
  }
  .label-range {
    width: 946px;
    height: 1200px;
    display: flex;
    align-items: center;
    justify-content: center;
    gap: 24px;
  }
  .label { width: 284px; height: 363px; display: block; }
  .label--plum { --ink: var(--plum); }
  .label--berry { --ink: var(--berry); }
  .label--tangerine { --ink: var(--tangerine); }

  .label-shape { fill: var(--label-base); stroke: var(--label-edge); stroke-width: 5; }
  .label-frame { fill: none; stroke: var(--ink); stroke-width: 1.6; }
  .wreath { fill: none; stroke: var(--ink); stroke-width: 24; stroke-opacity: 0.2; stroke-linecap: round; }
  .ink { fill: var(--ink); }
  .arc-tagline {
    font-family: "Barlow Condensed", sans-serif;
    font-weight: 500;
    font-size: 10px;
    letter-spacing: 4px;
  }
  .brand-name {
    font-family: "Barlow Condensed", sans-serif;
    font-weight: 500;
    font-size: 19px;
  }
  .product-name {
    font-family: "Kalam", cursive;
    font-weight: 700;
    font-size: 50px;
  }
  .volume {
    font-family: "Barlow Condensed", sans-serif;
    font-weight: 700;
    font-size: 9px;
  }
  .slogan {
    font-family: "Barlow Condensed", sans-serif;
    font-weight: 700;
    font-size: 10px;
    letter-spacing: 0.3px;
  }
</style>
</head>
<body>
<main class="label-range">

  <svg class="label label--plum" viewBox="0 0 270 345" aria-label="copper 71 Kombucha label, plum">
    <defs>
      <path id="plum-top-arc" d="M75,140 A60,60 0 0 1 195,140"/>
      <path id="plum-slogan-arc" d="M78,242 Q135,280 192,242"/>
    </defs>
    <path class="label-shape" d="M3,135 A132,132 0 0 1 267,135 L267,240 A132,102 0 0 1 3,240 Z"/>
    <path class="label-frame" d="M10,135 A125,125 0 0 1 260,135 L260,240 A125,95 0 0 1 10,240 Z"/>
    <g role="img" aria-label="Leaf wreath ornament">
      <path class="wreath" d="M30,140 A105,105 0 0 1 240,140"/>
      <path class="wreath" d="M30,218 A105,88 0 0 0 240,218"/>
    </g>
    <text class="arc-tagline ink"><textPath href="#plum-top-arc" startOffset="50%" text-anchor="middle">ARTISAN BEVERAGE</textPath></text>
    <text class="brand-name ink" x="135" y="140" text-anchor="middle">copper 71</text>
    <circle class="ink" cx="74" cy="146" r="3"/>
    <circle class="ink" cx="196" cy="146" r="3"/>
    <text class="product-name ink" x="135" y="200" text-anchor="middle" textLength="226" lengthAdjust="spacingAndGlyphs">Kombucha</text>
    <text class="volume ink" x="88" y="224" text-anchor="middle">4 FL OZ</text>
    <text class="volume ink" x="182" y="223" text-anchor="middle">120ML</text>
    <text class="slogan ink"><textPath href="#plum-slogan-arc" startOffset="50%" text-anchor="middle">DARE TO BE DELICIOUS</textPath></text>
  </svg>

  <svg class="label label--berry" viewBox="0 0 270 345" aria-label="copper 71 Kombucha label, berry">
    <defs>
      <path id="berry-top-arc" d="M75,140 A60,60 0 0 1 195,140"/>
      <path id="berry-slogan-arc" d="M78,242 Q135,280 192,242"/>
    </defs>
    <path class="label-shape" d="M3,135 A132,132 0 0 1 267,135 L267,240 A132,102 0 0 1 3,240 Z"/>
    <path class="label-frame" d="M10,135 A125,125 0 0 1 260,135 L260,240 A125,95 0 0 1 10,240 Z"/>
    <g role="img" aria-label="Leaf wreath ornament">
      <path class="wreath" d="M30,140 A105,105 0 0 1 240,140"/>
      <path class="wreath" d="M30,218 A105,88 0 0 0 240,218"/>
    </g>
    <text class="arc-tagline ink"><textPath href="#berry-top-arc" startOffset="50%" text-anchor="middle">ARTISAN BEVERAGE</textPath></text>
    <text class="brand-name ink" x="135" y="140" text-anchor="middle">copper 71</text>
    <circle class="ink" cx="74" cy="146" r="3"/>
    <circle class="ink" cx="196" cy="146" r="3"/>
    <text class="product-name ink" x="135" y="200" text-anchor="middle" textLength="226" lengthAdjust="spacingAndGlyphs">Kombucha</text>
    <text class="volume ink" x="88" y="224" text-anchor="middle">4 FL OZ</text>
    <text class="volume ink" x="182" y="223" text-anchor="middle">120ML</text>
    <text class="slogan ink"><textPath href="#berry-slogan-arc" startOffset="50%" text-anchor="middle">DARE TO BE DELICIOUS</textPath></text>
  </svg>

  <svg class="label label--tangerine" viewBox="0 0 270 345" aria-label="copper 71 Kombucha label, tangerine">
    <defs>
      <path id="tangerine-top-arc" d="M75,140 A60,60 0 0 1 195,140"/>
      <path id="tangerine-slogan-arc" d="M78,242 Q135,280 192,242"/>
    </defs>
    <path class="label-shape" d="M3,135 A132,132 0 0 1 267,135 L267,240 A132,102 0 0 1 3,240 Z"/>
    <path class="label-frame" d="M10,135 A125,125 0 0 1 260,135 L260,240 A125,95 0 0 1 10,240 Z"/>
    <g role="img" aria-label="Leaf wreath ornament">
      <path class="wreath" d="M30,140 A105,105 0 0 1 240,140"/>
      <path class="wreath" d="M30,218 A105,88 0 0 0 240,218"/>
    </g>
    <text class="arc-tagline ink"><textPath href="#tangerine-top-arc" startOffset="50%" text-anchor="middle">ARTISAN BEVERAGE</textPath></text>
    <text class="brand-name ink" x="135" y="140" text-anchor="middle">copper 71</text>
    <circle class="ink" cx="74" cy="146" r="3"/>
    <circle class="ink" cx="196" cy="146" r="3"/>
    <text class="product-name ink" x="135" y="200" text-anchor="middle" textLength="226" lengthAdjust="spacingAndGlyphs">Kombucha</text>
    <text class="volume ink" x="88" y="224" text-anchor="middle">4 FL OZ</text>
    <text class="volume ink" x="182" y="223" text-anchor="middle">120ML</text>
    <text class="slogan ink"><textPath href="#tangerine-slogan-arc" startOffset="50%" text-anchor="middle">DARE TO BE DELICIOUS</textPath></text>
  </svg>

</main>
</body>
</html>
```